Ember Quill Vitamin and Supplements site

I would like a design for vitamin and supplements website that will only stock the very best products. These vitamins will expensive. It needs to look distinct from the various vitamin, health and beauty websites. It needs to be simple and elegant, unisex, and with a mild/slight scientific feel. I will be choosing my products that are sold on my site based on great reviews and the tested science behind the products. This rigour should be reflected in the look and feel of the site.

I have a separate project for the coding the website, however I need further ideas on the design itself.

Target Market(s)

This site is for people who are willing to try new things and care deeply about their health.

Industry/Entity Type

Health And Wellness

```html
<!DOCTYPE html>
<html lang="en">
<head>
<meta charset="utf-8">
<title>Ember Quill — Vitamins &amp; Supplements</title>
<link href="https://fonts.googleapis.com/css2?family=Montserrat:wght@400;500;600&display=swap" rel="stylesheet">
<style>
  :root {
    --page: #e3e2e3;
    --panel: #ffffff;
    --ink: #2b2b2b;
    --teal: #5fcfc4;
    --muted: #c9c9c9;
  }
  * { margin: 0; padding: 0; box-sizing: border-box; }
  html, body { width: 1200px; height: 2326px; overflow: hidden; }
  body {
    background: var(--page);
    font-family: "Montserrat", sans-serif;
    color: var(--ink);
    letter-spacing: -0.04em;
    position: relative;
  }
  .sheet {
    position: absolute; left: 36px; top: 36px;
    width: 1128px; height: 2141px;
    background: var(--panel);
  }
  .brand {
    position: absolute; left: 86px; top: 185px;
    display: flex; align-items: center; gap: 10px;
    font-size: 24px; font-weight: 500; color: var(--teal);
  }
  .brand-dot { width: 14px; height: 14px; border-radius: 50%; background: var(--teal); }
  .main-nav {
    position: absolute; left: 601px; top: 122px;
    display: flex; gap: 22px; font-size: 17px;
  }
  .main-nav a { color: var(--ink); text-decoration: none; }
  .main-nav a.is-active { color: var(--teal); }
  .main-nav .plus { font-weight: 600; margin-left: 3px; }
  .intro {
    position: absolute; left: 86px; top: 437px; width: 930px;
    font-size: 23px; line-height: 38px; letter-spacing: -0.05em;
  }
  .intro strong { color: var(--teal); font-weight: 600; }
  .filters {
    position: absolute; right: 86px; top: 584px;
    display: flex; align-items: center; gap: 20px; font-size: 18px;
  }
  .filters .is-active { color: var(--teal); }
  .filters .sep { width: 3px; height: 3px; border-radius: 50%; background: var(--muted); }
  .gallery { position: absolute; left: 86px; top: 624px; width: 957px; height: 658px; }
  .tile { position: absolute; width: 319px; }
  .t1 { left: 0; top: 0; height: 219px; background: linear-gradient(135deg, #c9a77e 0%, #a7a7a6 45%, #d8d8d6 100%); }
  .t2 { left: 0; top: 219px; height: 439px; background: radial-gradient(ellipse at 50% 55%, #ffffff 0%, #eef0f0 40%, #7fcabf 62%, #e9eaea 78%); }
  .t3 { left: 319px; top: 0; height: 439px; background: linear-gradient(180deg, #e4e4e4 0%, #cfd1d1 35%, #2f9c89 70%, #ecebe8 100%); }
  .t4 { left: 319px; top: 439px; height: 219px; background: radial-gradient(ellipse at 50% 50%, #3fe0dc 0%, #7ad6cf 28%, #d3d0cb 60%); }
  .t5 { left: 638px; top: 0; height: 219px; background: linear-gradient(135deg, #bfc4c9 0%, #f4f4f4 50%, #aab0b5 100%); }
  .t6 { left: 638px; top: 219px; height: 439px; background: radial-gradient(ellipse at 50% 60%, #c65a4a 0%, #9bbf6a 25%, #f6f6f6 45%, #8fd9d6 60%, #ebebeb 80%); }
  .story { position: absolute; top: 1383px; width: 436px; font-size: 18px; line-height: 32.5px; letter-spacing: -0.05em; }
  .story h2 { font-size: 19px; font-weight: 600; line-height: 32px; }
  .story p + p { margin-top: 32px; }
  .story-left { left: 86px; }
  .story-right { left: 602px; }
  .more-btn {
    display: flex; align-items: center; justify-content: center;
    margin-top: 38px; width: 136px; height: 64px;
    border: 2px solid var(--teal); color: var(--teal); font-size: 18px;
    text-decoration: none;
  }
  .footer { position: absolute; left: 86px; top: 1928px; width: 957px; height: 40px; font-size: 15px; }
  .credit { position: absolute; left: 0; top: 8px; display: flex; align-items: center; gap: 3px; }
  .footer-brand { position: absolute; left: 0; right: 0; top: 6px; text-align: center; color: var(--teal); font-size: 18px; font-weight: 500; }
  .social { position: absolute; right: 0; top: 8px; display: flex; gap: 22px; }
  .social a { color: var(--ink); text-decoration: none; }
</style>
</head>
<body>
  <main class="sheet">
    <div class="brand"><span class="brand-dot"></span>Ember Quill</div>
    <nav class="main-nav">
      <a class="is-active" href="#">Home<span class="plus">+</span></a>
      <a href="#">About</a>
      <a href="#">Products</a>
      <a href="#">Blog</a>
      <a href="#">Contact<span class="plus">+</span></a>
    </nav>

    <p class="intro"><strong>Together for a healthier world.</strong> We're bringing the best brands together, based on the greater reviews and on tested science behind the products.</p>

    <div class="filters">
      <span class="is-active">All</span><span class="sep"></span>
      <span>Post</span><span class="sep"></span>
      <span>Image</span><span class="sep"></span>
      <span>Video</span><span class="sep"></span>
      <span>Extern</span>
    </div>

    <section class="gallery">
      <div class="tile t1" role="img" aria-label="Amber dropper bottles, leaves and sponge on a wooden tray over grey stone"></div>
      <div class="tile t2" role="img" aria-label="White pouch of premium wraps with a teal label"></div>
      <div class="tile t3" role="img" aria-label="Grey jar of probiotic capsules with a teal lid and band"></div>
      <div class="tile t4" role="img" aria-label="Glossy turquoise sachet on a beige surface"></div>
      <div class="tile t5" role="img" aria-label="White capsules in a silver blister pack"></div>
      <div class="tile t6" role="img" aria-label="White supplement jar with a turquoise lid and apple label"></div>
    </section>

    <article class="story story-left">
      <h2>The Story</h2>
      <p>With a warning label this big, you know they gotta be fun. Bring me the forms I need to fill out to have her taken away. I decline the title of iron cook and accept the lesser title of zinc saucier, which I just made up.</p>
      <p>Curabitur felis mi, sodales id ligula ac, pulvinar condimentum nulla. Integer dignissim bibendum augue, id dapibus nisl maximus non. Pellentesque rhoncus vitae odio ut euismod.</p>
    </article>

    <article class="story story-right">
      <h2>Dreamers</h2>
      <p>You probably haven’t heard of them before they sold out scenester literally readymade. Trust fund Pinewhistle flexitarian, aesthetic Fernly banjo freegan semiotics biodiesel master cleanse taxidermy blog.</p>
      <a class="more-btn" href="#">More...</a>
    </article>

    <footer class="footer">
      <div class="credit">© 2021
        <svg width="15" height="13" viewBox="0 0 24 21" aria-hidden="true"><path d="M12 21 2 11A6 6 0 0 1 12 3a6 6 0 0 1 10 8z" fill="#5fcfc4"/></svg>
        by Larkfield.</div>
      <div class="footer-brand">Ember Quill</div>
      <nav class="social">
        <a href="#">Chirper</a>
        <a href="#">Linkwork</a>
        <a href="#">Shotboard</a>
        <a href="#">Picturely</a>
      </nav>
    </footer>
  </main>
</body>
</html>
```